The Velorind Project

All information regarding the design is located at Velorind.com. Any questions regarding the project, will be answered on the site.

```html
<!DOCTYPE html>
<html lang="en">
<head>
<meta charset="utf-8">
<title>Velorind</title>
<link rel="stylesheet" href="https://fonts.googleapis.com/css2?family=Arimo:wght@400&family=Open+Sans:wght@400;600&display=swap">
<style>
  :root {
    --page-bg: #ffffff;
    --page-fade: #f1f1f1;
    --nav-top: #ffffff;
    --nav-bottom: #f3f3f3;
    --nav-border: #e4e4e4;
    --tab-active: #e0e0e0;
    --text-nav: #555555;
    --text-dark: #222222;
    --brand-blue: #4a86e8;
    --field-border: #cfcfcf;
    --field-top: #e9e9e9;
    --field-bottom: #ffffff;
    --btn-top: #a8d81a;
    --btn-bottom: #8cc20a;
    --btn-text: #3e5a06;
  }
  * { box-sizing: border-box; margin: 0; padding: 0; }
  html, body { width: 1200px; height: 642px; overflow: hidden; }
  body {
    position: relative;
    font-family: "Arimo", Arial, sans-serif;
    background: linear-gradient(to bottom, var(--page-bg) 0%, var(--page-bg) 66%, var(--page-fade) 100%);
  }
  .main-nav {
    position: absolute; left: 0; top: 0; width: 1200px; height: 46px;
    background: linear-gradient(to bottom, var(--nav-top), var(--nav-bottom));
    border-bottom: 1px solid var(--nav-border);
  }
  .main-nav a {
    position: absolute; top: 0; height: 46px; line-height: 44px;
    font-size: 17px; color: var(--text-nav); text-decoration: none;
    transform: translateX(-50%); white-space: nowrap;
  }
  .main-nav a.is-active {
    left: 0; width: 100px; transform: none; text-align: center;
    background: var(--tab-active); color: var(--text-dark);
  }
  .account-links {
    position: absolute; left: 1027px; top: 70px; width: 154px; height: 39px;
    border: 1px solid #e2e2e2; border-radius: 4px;
    background: linear-gradient(to bottom, #ffffff, #f2f2f2);
    font-size: 16px; color: var(--text-nav);
    display: flex; align-items: center; justify-content: center; gap: 10px;
  }
  .brand-name {
    position: absolute; left: 0; width: 1122px; top: 190px;
    text-align: center;
    font-family: "Open Sans", sans-serif; font-weight: 600;
    font-size: 100px; line-height: 120px; letter-spacing: 4px;
    color: var(--brand-blue);
  }
  .advanced-search {
    position: absolute; right: 291px; top: 306px;
    font-size: 16px; color: var(--text-dark);
  }
  .search-form { position: absolute; left: 207px; top: 342px; display: flex; }
  .search-field {
    width: 622px; height: 43px;
    border: 1px solid var(--field-border); border-right: none;
    background: linear-gradient(to bottom, var(--field-top), var(--field-bottom));
  }
  .search-button {
    width: 130px; height: 43px; border: 1px solid #8ab90c;
    background: linear-gradient(to bottom, var(--btn-top), var(--btn-bottom));
    font-family: "Open Sans", sans-serif; font-size: 17px; letter-spacing: 0.5px;
    color: var(--btn-text);
    display: flex; align-items: center; justify-content: center;
  }
  .site-footer {
    position: absolute; left: 0; width: 1122px; top: 418px;
    text-align: center; font-size: 15.5px; color: var(--text-dark);
  }
</style>
</head>
<body>
  <nav class="main-nav">
    <a class="is-active" href="#">List</a>
    <a href="#" style="left:178px">Step by step</a>
    <a href="#" style="left:322px">Image</a>
    <a href="#" style="left:426px">Link</a>
    <a href="#" style="left:521px">Text</a>
    <a href="#" style="left:663px">Video(Streamora)</a>
  </nav>

  <div class="account-links"><span>Sign up</span><span>|</span><span>Log in</span></div>

  <h1 class="brand-name">Velorind</h1>

  <div class="advanced-search">Advanced Search Box...</div>

  <div class="search-form">
    <div class="search-field"></div>
    <div class="search-button">SEARCH</div>
  </div>

  <footer class="site-footer">© 2010 Copyright | About &nbsp;| Privacy | Legal | Help | Feedback</footer>
</body>
</html>
```